Cloud Phone Service Brochure

We need a brochure for a Cloud Phone Service offering that we offer in Canada. We're a small company that cares about our client's success and protects their privacy. We would like to see designs that reflect us as a stable, trustworthy company which is also fast moving and leading edge. We see ourselves more like Quenby than Harn. Mosaic Vault has built our logo and business card, and we look forward to moving ahead here. I've attached our Business Card file so you have our logo as well as my own shot at some thoughts about content written as a trifold. That specific content does not need to be used, nor does it need to be a trifold. Those phone pictures are the actual phones we use.

```html
<!DOCTYPE html>
<html lang="en">
<head>
<meta charset="utf-8">
<title>Brightline Consulting – Cloud Phone Service Brochure</title>
<link rel="stylesheet" href="https://fonts.googleapis.com/css2?family=Montserrat:wght@400;500;600;700&family=Oswald:wght@300;400;700&display=swap">
<style>
:root{
  --blue:#1b8ad6;
  --blue-dark:#0f6fb4;
  --ink:#2e3135;
  --ink-soft:#55595e;
  --paper:#ffffff;
  --paper-shade:#eef0f2;
  --stage:#e4e6e9;
  --photo-brown:#5a3a28;
  --photo-warm:#c9782a;
  --photo-cool:#8fa6bd;
  --photo-navy:#1f2b3d;
}
*{margin:0;padding:0;box-sizing:border-box}
html,body{width:1200px;height:2190px;overflow:hidden}
body{background:var(--stage);font-family:"Montserrat",Arial,sans-serif;color:var(--ink);position:relative}
.spread{position:absolute;left:40px;width:1120px;height:866px;background:var(--paper);box-shadow:0 10px 30px rgba(0,0,0,.18);display:flex}
.spread--outside{top:120px}
.spread--inside{top:1100px}
.panel{position:relative;width:373.33px;height:100%;overflow:hidden}
.panel + .panel{border-left:1px solid var(--paper-shade)}
.photo{position:absolute;display:block}
svg.shape{position:absolute;left:0;display:block}
.heading{font-family:"Oswald",Arial,sans-serif;font-weight:700;text-transform:uppercase;font-size:19px;line-height:1.1;color:var(--ink);letter-spacing:.3px}
.heading span{color:var(--blue);display:block}
.heading--inline span{display:inline}
.list{list-style:none;font-size:12.5px;line-height:1.55;color:var(--ink-soft)}
.list li{position:relative;padding-left:18px}
.list li::before{content:"";position:absolute;left:0;top:6px;width:9px;height:9px;background:var(--blue);border-radius:2px}
.list--sub{padding-left:18px}
.list--sub li{padding-left:14px}
.list--sub li::before{background:none;border:1.5px solid var(--blue);border-radius:50%;width:7px;height:7px;top:7px}
.brand{display:flex;align-items:center;gap:10px;font-family:"Montserrat",Arial,sans-serif;font-weight:600;font-size:15px;color:var(--blue);letter-spacing:1px;text-transform:uppercase;white-space:nowrap}
.brand__mark{width:26px;height:26px;background:var(--blue);flex:none}

/* outside – back flap */
.partners{position:absolute;left:34px;top:250px;right:34px}
.badges{display:grid;grid-template-columns:repeat(3,1fr);gap:12px;margin:14px 0 26px}
.badge{height:36px;border-radius:6px;background:var(--paper);box-shadow:0 1px 4px rgba(0,0,0,.25);display:flex;align-items:center;justify-content:center}
.badge i{display:block;width:60%;height:14px;border-radius:3px;background:#cfd4da}
.block-title{font-family:"Oswald",Arial,sans-serif;font-weight:700;text-transform:uppercase;font-size:15px;color:var(--ink);margin-bottom:4px}
.block-title span{color:var(--blue)}
.partners .list{font-style:italic;margin-bottom:18px}

/* outside – back panel */
.contact{position:absolute;left:0;right:0;top:300px;text-align:center}
.contact .brand{justify-content:center;margin-bottom:34px}
.contact__item{font-size:15px;color:var(--ink);margin-bottom:22px;line-height:1.45}
.contact__item svg{display:block;margin:0 auto 6px}

/* outside – cover */
.cover .brand{position:absolute;right:34px;top:30px;font-size:13px;gap:8px}
.cover .brand__mark{width:22px;height:22px}
.cover__title{position:absolute;left:34px;right:24px;top:620px;font-family:"Oswald",Arial,sans-serif;text-transform:uppercase;white-space:nowrap}
.cover__title strong{display:block;font-weight:700;font-size:44px;color:var(--ink);line-height:1}
.cover__title em{display:block;font-style:normal;font-weight:300;font-size:33px;color:var(--blue);line-height:1.2}
.cover__web{position:absolute;left:34px;top:748px;font-size:16px;font-weight:500;color:var(--ink);letter-spacing:.5px}

/* inside */
.copy{position:absolute;left:34px;right:30px}
.copy .heading{margin-bottom:10px}
.copy .list{margin-bottom:22px}
</style>
</head>
<body>

<section class="spread spread--outside" aria-label="Brochure outside">

  <div class="panel panel--flap">
    <div class="photo" role="img" aria-label="Photo of the desk phones with colour video screens" style="left:0;top:0;width:373px;height:215px;background:linear-gradient(135deg,#1d2026 0%,#3b4250 55%,#9aa6b4 100%)"></div>
    <svg class="shape" style="top:150px" width="374" height="110" viewBox="0 0 374 110">
      <path d="M0 20 C120 60 250 70 374 30 L374 110 L0 110 Z" fill="var(--paper)"/>
      <path d="M0 20 C120 60 250 70 374 30 L374 46 C250 86 120 76 0 36 Z" fill="var(--blue)"/>
    </svg>
    <div class="partners">
      <p class="heading">Our <span>Partners</span></p>
      <div class="badges">
        <div class="badge"><i></i></div><div class="badge"><i></i></div><div class="badge"><i></i></div>
        <div class="badge"><i></i></div><div class="badge"><i></i></div><div class="badge"><i></i></div>
        <div class="badge"><i></i></div><div class="badge"><i></i></div><div class="badge"><i></i></div>
      </div>
      <p class="block-title">We <span>are</span></p>
      <ul class="list">
        <li>70% Renewable Energy</li>
        <li>100% Renewable for 2020</li>
      </ul>
      <p class="block-title">We give our time and <span>skills to help</span></p>
      <ul class="list">
        <li>Schools</li>
        <li>Community Associations</li>
        <li>Non-profits</li>
        <li>Renewable Energy Initiatives</li>
      </ul>
    </div>
  </div>

  <div class="panel panel--back">
    <div class="contact">
      <div class="brand"><span class="brand__mark"></span>Brightline Consulting</div>
      <p class="contact__item">
        <svg width="22" height="22" viewBox="0 0 24 24"><path fill="var(--blue)" d="M6.6 10.8a15 15 0 0 0 6.6 6.6l2.2-2.2c.3-.3.7-.4 1-.2 1.1.4 2.3.6 3.6.6.6 0 1 .4 1 1V20c0 .6-.4 1-1 1A17 17 0 0 1 3 4c0-.6.4-1 1-1h3.5c.6 0 1 .4 1 1 0 1.3.2 2.5.6 3.6.1.3 0 .7-.2 1z"/></svg>
        (306) 555-0182
      </p>
      <p class="contact__item">
        <svg width="22" height="22" viewBox="0 0 24 24"><circle cx="12" cy="12" r="9" fill="none" stroke="var(--blue)" stroke-width="2"/><path d="M3 12h18M12 3c3 3 3 15 0 18M12 3c-3 3-3 15 0 18" fill="none" stroke="var(--blue)" stroke-width="1.6"/></svg>
        www.brightlineconsult.ca
      </p>
      <p class="contact__item">
        <svg width="22" height="22" viewBox="0 0 24 24"><path fill="var(--blue)" d="M12 2a7 7 0 0 0-7 7c0 5 7 13 7 13s7-8 7-13a7 7 0 0 0-7-7zm0 9.5A2.5 2.5 0 1 1 12 6.5a2.5 2.5 0 0 1 0 5z"/></svg>
        PO Box 30218<br>14-4410 Ridgeview Lane<br>Pinecrest, Saskatchewan S4N 7B2<br>Canada
      </p>
    </div>
  </div>

  <div class="panel panel--cover cover">
    <div class="brand"><span class="brand__mark"></span>Brightline Consulting</div>
    <svg class="shape" style="top:80px" width="374" height="500" viewBox="0 0 374 500">
      <path d="M0 300 L70 300 L150 440 L374 440 L374 470 L170 470 L210 500 L0 500 Z" fill="var(--blue)"/>
    </svg>
    <div class="photo" role="img" aria-label="Photo of open hands holding a glowing light beneath orange cloud icons with hanging device symbols" style="left:0;top:80px;width:374px;height:440px;clip-path:polygon(0 0,100% 0,100% 100%,40% 100%,19% 68%,0 68%);background:radial-gradient(circle at 55% 62%,#ffd27a 0%,var(--photo-warm) 18%,var(--photo-brown) 50%,#2d1e16 100%)"></div>
    <div class="cover__title"><strong>Get Connected</strong><em>Anywhere Anytime!</em></div>
    <p class="cover__web">www.brightlineconsult.ca</p>
    <svg class="shape" style="top:826px" width="374" height="40" viewBox="0 0 374 40"><path d="M120 0 L374 0 L374 40 L90 40 Z" fill="var(--blue)"/></svg>
  </div>
</section>

<section class="spread spread--inside" aria-label="Brochure inside">

  <div class="panel">
    <div class="photo" role="img" aria-label="Photo of a bright video conference room with a wall screen showing remote colleagues" style="left:0;top:0;width:373px;height:240px;background:linear-gradient(160deg,#f3f5f7 0%,#d8dee5 55%,#b9c3cd 100%)"></div>
    <svg class="shape" style="top:180px" width="374" height="90" viewBox="0 0 374 90">
      <path d="M0 40 C130 10 250 20 374 60 L374 90 L0 90 Z" fill="var(--paper)"/>
      <path d="M0 40 C130 10 250 20 374 60 L374 74 C250 34 130 24 0 54 Z" fill="var(--blue)"/>
    </svg>
    <div class="copy" style="top:290px">
      <p class="heading">Why cloud <span>service?</span></p>
      <ul class="list">
        <li>Cloud Phones mean no setup costs and no hardware to purchase or support.</li>
        <li>Cloud service also offers seamless remote working and multi-office collaboration.</li>
      </ul>
      <p class="heading heading--inline">Why <span>Brightline?</span></p>
      <ul class="list">
        <li>Brightline believes in building long term collaborative relationships.</li>
        <li>We care about your business as if it was our own.</li>
        <li>Your privacy matters to us. We do not sell, rent or share your data.</li>
      </ul>
    </div>
    <svg class="shape" style="top:650px" width="374" height="50" viewBox="0 0 374 50">
      <path d="M0 50 L0 20 C120 0 260 10 374 40 L374 50 Z" fill="var(--blue)"/>
    </svg>
    <div class="photo" role="img" aria-label="Photo of a businessman holding a tablet beneath blue cloud icons" style="left:0;top:672px;width:373px;height:194px;clip-path:polygon(0 0,45% 0,100% 12%,100% 100%,0 100%);background:linear-gradient(135deg,var(--photo-navy) 0%,#3f6a95 50%,var(--photo-cool) 100%)"></div>
  </div>

  <div class="panel">
    <div class="copy" style="top:40px">
      <p class="heading">Video conferencing <span>room configuration</span></p>
      <ul class="list">
        <li>120 Simultaneous video streams supported</li>
        <li>Most conference sources
          <ul class="list list--sub">
            <li>Video Conf Room System</li>
            <li>Video Phones</li>
            <li>Desktop &amp; Laptop Computers</li>
            <li>Phone &amp; Tablet Devices</li>
            <li>SIP PBXes</li>
            <li>PSTN Phones</li>
          </ul>
        </li>
        <li>Connect Video &amp; Social Live</li>
        <li>1080p HD at 30 fps</li>
        <li>Multi-location conferencing</li>
        <li>Meeting Controls</li>
        <li>Screen Sharing</li>
        <li>Customizable Registration options</li>
        <li>Email Follow-up options</li>
        <li>10 simultaneous sessions</li>
        <li>Encrypted connections</li>
      </ul>
    </div>
    <div class="photo" role="img" aria-label="Photo of a black conference camera" style="left:220px;top:510px;width:110px;height:55px;border-radius:50%;background:radial-gradient(circle at 50% 40%,#555 0%,#1b1b1d 70%)"></div>
    <div class="copy" style="top:580px">
      <p class="heading">Phone <span>service features:</span></p>
      <ul class="list">
        <li>All features and functions included</li>
        <li>Conference line included</li>
        <li>Toll Free Number included</li>
        <li>North American LD included</li>
        <li>Monthly billing with no contract</li>
        <li>No hardware or installation costs</li>
        <li>Any high speed internet service</li>
        <li>Keep your existing phone number</li>
        <li>Voicemail to email</li>
        <li>Find Me &amp; Follow Me</li>
        <li>Call Recording</li>
      </ul>
    </div>
  </div>

  <div class="panel">
    <div class="photo" role="img" aria-label="Photo of a black desk phone with a colour display" style="left:250px;top:20px;width:100px;height:80px;border-radius:8px;background:linear-gradient(160deg,#3a3d42 0%,#111 100%)"></div>
    <div class="copy" style="top:40px">
      <p class="heading">Our <span>services</span></p>
      <ul class="list" style="margin-top:36px">
        <li>Network Support</li>
        <li>Phone Service</li>
        <li>Disaster Recovery</li>
        <li>Remote Backups</li>
        <li>Email Archiving</li>
        <li>Office Suite &amp; Cloud Apps</li>
        <li>Migration Services</li>
        <li>Spam and Virus Filtering</li>
        <li>Server and Network Monitoring</li>
        <li>Printing, Scanning and Plotting</li>
        <li>Firewalls and Security</li>
        <li>Network Design and Planning</li>
        <li>Network and Electrical Cabling</li>
        <li>Wireless coverage planning</li>
        <li>Security cameras &amp; Access Control</li>
      </ul>
    </div>
    <svg class="shape" style="top:560px" width="374" height="60" viewBox="0 0 374 60">
      <path d="M0 60 L0 50 C140 50 260 30 374 0 L374 60 Z" fill="var(--blue)"/>
    </svg>
    <div class="photo" role="img" aria-label="Photo of a businessman holding a glowing globe made of media screens" style="left:0;top:585px;width:373px;height:281px;clip-path:polygon(0 12%,50% 8%,100% 0,100% 100%,0 100%);background:radial-gradient(circle at 35% 55%,#9ab6d2 0%,#3f5f85 30%,var(--photo-navy) 65%,#0e141d 100%)"></div>
  </div>
</section>

</body>
</html>
```